TLB Shark card

This is a serious business card for a retired attorney with a sarcastic sense of humor. Incorporate into the design: shark with the tag line, Gentle until challenged. The image could be graphic but not comic. The card should have a classic, sophisticated, professional look. Partial to minimalist, even Asian designs. Color options are black/ white (though this can easily go too cartoonish), gray tones, blue gray tones, blue. Open to something unexpected, even color, as long as the look is professional. The shark image attached is what we've been using but it isn't a design requirement.(Not sure why entire image isn't visible.)
Updates

No company Howard L Brisbane Name should be more prominent than the tag

This is the first time I've done this, so I apologize for not posting all this info up front. Some of it was in the narrative but to make it easier, I'm listing all the info that should be on the card. Howard L Brisbane Attorney at Law shark image Gentle until challenged 27815 Velvet Harbor Street Dana Point, CA 92631 555-814-2073 hbrisbane@quellmail.net There is no company. The tag, Gentle until challenged, should be less prominent than the name.

Industry/Entity Type

Attorney

Contact Information for Business Card

27815 Velvet Harbor Street
Dana Point, CA 92631
555-814-2073
hbrisbane@quellmail.net

```html
<!DOCTYPE html>
<html lang="en">
<head>
<meta charset="utf-8">
<title>TLB Shark card</title>
<link rel="stylesheet" href="https://fonts.googleapis.com/css2?family=Cinzel:wght@400&family=Crimson+Pro:wght@600&family=Tinos&display=swap">
<style>
  :root {
    --backdrop: #e6e3df;
    --card: #000000;
    --card-edge: #2b2b2b;
    --ink: #ffffff;
    --ink-soft: #c9c9c9;
    --ink-muted: #d6d6d6;
    --art-light: #5a5a5a;
    --art-dark: #111111;
  }
  html, body {
    margin: 0;
    padding: 0;
    width: 1200px;
    height: 1200px;
    overflow: hidden;
    background: var(--backdrop);
  }
  .canvas {
    position: relative;
    width: 1200px;
    height: 1200px;
  }
  .business-card {
    position: absolute;
    left: 280px;
    top: 30px;
    width: 640px;
    height: 1140px;
    box-sizing: border-box;
    background: var(--card);
    border: 6px solid var(--card-edge);
    color: var(--ink);
    text-align: center;
  }
  .business-card > * {
    position: absolute;
    left: 0;
    right: 0;
    margin: 0;
  }
  .shark-art {
    top: 70px;
    left: 70px;
    right: 70px;
    height: 190px;
    border-radius: 50%;
    background: radial-gradient(ellipse at center, var(--art-light) 0%, var(--art-dark) 70%, var(--card) 100%);
  }
  .profession {
    top: 286px;
    font-family: "Cinzel", serif;
    font-weight: 400;
    font-size: 54px;
    line-height: 62px;
    letter-spacing: 1px;
  }
  .tagline {
    top: 352px;
    font-family: "Cinzel", serif;
    font-size: 21px;
    line-height: 26px;
    letter-spacing: 1.5px;
    color: var(--ink-soft);
  }
  .holder-name {
    top: 566px;
    font-family: "Crimson Pro", serif;
    font-weight: 600;
    font-size: 46px;
    line-height: 56px;
  }
  .contact {
    top: 806px;
    font-family: "Tinos", serif;
    font-size: 42px;
    line-height: 58px;
  }
  .contact p { margin: 0; }
  .address {
    top: 934px;
    font-family: "Tinos", serif;
    font-style: normal;
    font-size: 35px;
    line-height: 44px;
    color: var(--ink-muted);
  }
  .address p { margin: 0; }
</style>
</head>
<body>
<div class="canvas">
  <section class="business-card">
    <div class="shark-art" role="img" aria-label="Line illustration of a shark swimming to the right, white strokes on black"></div>
    <h1 class="profession">Attorney at Law</h1>
    <p class="tagline">Gentle until challenged</p>
    <h2 class="holder-name">Howard L Brisbane</h2>
    <div class="contact">
      <p class="phone">555-814-2073</p>
      <p class="email">hbrisbane@quellmail.net</p>
    </div>
    <address class="address">
      <p>Gentle until challenged 27815</p>
      <p>Velvet Harbor Street</p>
      <p>Coral Bluff, CA 92631</p>
    </address>
  </section>
</div>
</body>
</html>
```